Vardel coatings banner

Banner same size Brisk Hallways advert banner
of previous one Brisk Hallways advert banner 215cm x 1055cm
but for a paint company, called Vardel Coatings.
I want the concept to be similar to the attached, i want to put some real drum paint in front of the banner concept to look in Harmony with your concept on the banner.
The company is specialized in producing and painting houses and offices indoor and outdoor and applying epoxy on floors..

```html
<!DOCTYPE html>
<html lang="en">
<head>
<meta charset="utf-8">
<title>Vardel Coatings Banner</title>
<link href="https://fonts.googleapis.com/css2?family=Lato:wght@400;700;900&display=swap" rel="stylesheet">
<style>
  :root {
    --wall-light: #a9b6c4;
    --wall-dark: #7d8ea0;
    --brand-blue: #2f7dc4;
    --tick-blue: #2f6fb5;
    --plaster-light: #f7f7f7;
    --plaster-mid: #e6e6e6;
    --ink: #333a40;
    --white: #ffffff;
    --paint-red: #c8102e;
    --paint-purple: #8a2be2;
  }
  html, body {
    margin: 0;
    padding: 0;
    overflow: hidden;
    background: var(--white);
  }
  .banner {
    position: relative;
    width: 1200px;
    height: 245px;
    overflow: hidden;
    font-family: "Lato", Arial, sans-serif;
    background: radial-gradient(ellipse at 70% 40%, var(--plaster-light) 0%, var(--plaster-mid) 100%);
  }
  .banner-shapes {
    position: absolute;
    inset: 0;
  }
  .brand-name {
    position: absolute;
    left: 92px;
    top: 68px;
    margin: 0;
    color: var(--white);
    font-weight: 900;
    font-size: 46px;
    line-height: 44px;
    letter-spacing: 0.5px;
    text-transform: uppercase;
  }
  .service-list {
    position: absolute;
    left: 660px;
    top: 64px;
    margin: 0;
    padding: 0;
    list-style: none;
    color: var(--ink);
    font-size: 22px;
    line-height: 29px;
  }
  .service-item {
    position: relative;
    padding-left: 34px;
    margin-bottom: 10px;
    width: 400px;
  }
  .service-tick {
    position: absolute;
    left: 0;
    top: 5px;
    width: 20px;
    height: 20px;
  }
  .paint-pour {
    position: absolute;
    right: 0;
    top: 0;
    width: 150px;
    height: 225px;
    background:
      radial-gradient(ellipse 40px 100px at 35% 55%, var(--paint-red) 0%, rgba(200,16,46,0) 100%),
      radial-gradient(ellipse 40px 100px at 75% 50%, var(--paint-purple) 0%, rgba(138,43,226,0) 100%);
  }
  .print-code {
    position: absolute;
    right: 8px;
    bottom: 4px;
    font-size: 12px;
    color: var(--ink);
  }
</style>
</head>
<body>
  <div class="banner">
    <svg class="banner-shapes" width="1200" height="245" viewBox="0 0 1200 245">
      <defs>
        <linearGradient id="wallTone" x1="0" y1="0" x2="1" y2="1">
          <stop offset="0" stop-color="var(--wall-light)"/>
          <stop offset="1" stop-color="var(--wall-dark)"/>
        </linearGradient>
      </defs>
      <path class="wall-scene" role="img" aria-label="Grey wall with colourful paint dripping down onto the floor"
            d="M0,0 H485 C468,70 520,140 580,195 C610,222 625,240 632,245 H0 Z" fill="url(#wallTone)"/>
      <path class="brand-wave"
            d="M485,0 H505 C495,80 560,150 620,200 C645,222 665,238 680,245 H632 C625,240 610,222 580,195 C520,140 468,70 485,0 Z"
            fill="var(--brand-blue)"/>
    </svg>

    <h1 class="brand-name">Vardel<br>Coatings</h1>

    <ul class="service-list">
      <li class="service-item">
        <svg class="service-tick" viewBox="0 0 20 20"><circle cx="10" cy="10" r="8.5" fill="none" stroke="var(--tick-blue)" stroke-width="2"/><path d="M6,10.5 L9,13 L14,7.5" fill="none" stroke="var(--tick-blue)" stroke-width="2.2" stroke-linecap="round" stroke-linejoin="round"/></svg>
        Painting houses and offices indoor and outdoor
      </li>
      <li class="service-item">
        <svg class="service-tick" viewBox="0 0 20 20"><circle cx="10" cy="10" r="8.5" fill="none" stroke="var(--tick-blue)" stroke-width="2"/><path d="M6,10.5 L9,13 L14,7.5" fill="none" stroke="var(--tick-blue)" stroke-width="2.2" stroke-linecap="round" stroke-linejoin="round"/></svg>
        Applying epoxy on the floor
      </li>
    </ul>

    <div class="paint-pour" role="img" aria-label="Two paint cans pouring red and purple paint into puddles"></div>

    <span class="print-code">C50</span>
  </div>
</body>
</html>
```